Wedding Music Playlist Template

Hi, I'm a wedding musician and I'd like a 1 pager wedding music template created. It needs to be editable for future weddings.

At the top of the template:
Bride First Name & Groom First Name plus 's WEDDING
Date of Wedding:
Venue name:

(The form needs to be flexible where I can remove/interchange Prelude Ceremony / Ceremony / Canapes / Reception) as sometimes I will play music just for a Ceremony sometimes for both Ceremony/Canapes or sometimes just the reception only or all of the above.

Section 1: Prelude Ceremony (this could be up to 5 songs)

Section 2: Ceremony
Processional (this is sometimes 1 or 2 songs)
Signing of Papers (this is sometimes 1 or 2 songs)
Recessional (1 song)

Section 3: Canapes

Section 4: Reception

Within each section
Artist
Song

I'd also like the template to feature
logo (attached) and social media links
website URL tolvercade.com.au
instagram: tolvercademusic
facebook: tolvercadepianist
soundcloud: keyglow_nuptials

I see the form/template serving two purposes.
1) I'll send back to the bride when she books me for a wedding and she may socialise it.
2) Posting on instagram as I perform at each wedding and attract engaged brides looking for wedding pianist or even just ideas for wedding music.
Updates

Target Market(s)

Engaged Couples looking for wedding music or suggested music for wedding

Industry/Entity Type

Wedding

Requirements
Must have
• Please see project description.
Nice to have
• Background wedding image with text overlayed

```html
<!DOCTYPE html>
<html lang="en">
<head>
<meta charset="utf-8">
<title>Anna &amp; John's Wedding – Music Programme</title>
<link rel="stylesheet" href="https://fonts.googleapis.com/css2?family=Great+Vibes&family=Cormorant+Garamond:wght@400;500&family=Open+Sans:wght@400;600;700&display=swap">
<style>
  :root {
    --cream: #f8ede2;
    --cream-light: #fdf6ee;
    --copper: #b5773f;
    --copper-dark: #9a6232;
    --pill: #c48d58;
    --ink: #3a2a20;
    --footer: #2b211c;
    --white: #ffffff;
  }
  * { box-sizing: border-box; margin: 0; padding: 0; }
  html, body { width: 849px; height: 1200px; overflow: hidden; background: var(--cream); }
  .sheet {
    position: relative; width: 849px; height: 1200px; overflow: hidden;
    background: linear-gradient(180deg, var(--cream-light) 0%, var(--cream) 60%, #f1dfcc 100%);
    font-family: "Open Sans", sans-serif; color: var(--ink);
  }
  .hero-photo {
    position: absolute; left: 0; top: 0; width: 849px; height: 300px;
    background: linear-gradient(100deg, #a79b86 0%, #d8d2c4 35%, #5a5048 65%, #2a2622 85%, #8a8478 100%);
  }
  .hero-curve { position: absolute; left: 0; top: 190px; width: 849px; height: 112px; }
  .couple-photo {
    position: absolute; left: 0; top: 780px; width: 660px; height: 370px;
    background: radial-gradient(ellipse at 40% 60%, rgba(233,214,196,.95) 0%, rgba(214,190,170,.8) 35%, rgba(248,237,226,0) 72%),
                radial-gradient(ellipse at 10% 90%, rgba(206,140,150,.55) 0%, rgba(248,237,226,0) 40%);
  }
  .title { position: absolute; left: 40px; top: 318px; width: 400px; height: 150px; }
  .title .name { font-family: "Great Vibes", cursive; font-size: 66px; color: var(--copper); line-height: 1; position: absolute; }
  .title .bride { left: 12px; top: 0; }
  .title .amp { font-family: "Great Vibes", cursive; font-size: 110px; color: #e6c9a8; position: absolute; left: 150px; top: -30px; line-height: 1.2; opacity: .8; }
  .title .groom { left: 200px; top: 22px; }
  .title .event { font-family: "Cormorant Garamond", serif; font-size: 46px; color: var(--copper); position: absolute; left: 95px; top: 92px; line-height: 1.2; }
  .details { position: absolute; left: 445px; top: 402px; width: 380px; }
  .details .date { font-size: 30px; font-weight: 600; color: var(--ink); line-height: 1.3; }
  .details .venue { font-size: 19px; font-weight: 600; margin-top: 14px; margin-left: 100px; }
  .details .address { font-size: 13px; margin-left: 60px; }
  .section { position: absolute; width: 300px; }
  .pill {
    width: 275px; height: 34px; border-radius: 17px; background: var(--pill);
    color: var(--white); font-size: 19px; font-weight: 600; text-align: center; line-height: 34px;
    margin-bottom: 13px;
  }
  .ceremony .pill { margin-bottom: 18px; }
  .song { font-size: 15px; color: var(--copper-dark); line-height: 30px; padding-left: 8px; white-space: nowrap; }
  .song .sep { margin: 0 8px; }
  .part { font-size: 17px; font-weight: 400; color: var(--pill); padding-left: 8px; line-height: 28px; }
  .prelude { left: 48px; top: 553px; }
  .canapes { left: 48px; top: 798px; }
  .ceremony { left: 485px; top: 553px; }
  .reception { left: 485px; top: 900px; }
  .brand { position: absolute; left: 487px; top: 1050px; display: flex; align-items: center; gap: 12px; }
  .brand .mark { width: 56px; height: 56px; border-radius: 50%; background: var(--ink); }
  .brand .name { font-size: 30px; font-weight: 700; color: var(--ink); letter-spacing: 1px; }
  .web { position: absolute; left: 555px; top: 1112px; font-size: 18px; font-weight: 600; color: var(--ink); }
  .footer {
    position: absolute; left: 0; bottom: 0; width: 849px; height: 48px; background: var(--footer);
    display: flex; align-items: center; justify-content: space-around; padding: 0 20px;
  }
  .footer .link { display: flex; align-items: center; gap: 8px; color: #e8dccf; font-size: 12.5px; }
  .footer .dot { width: 22px; height: 22px; border-radius: 4px; background: #6b5a4d; }
</style>
</head>
<body>
<main class="sheet">
  <div class="hero-photo" role="img" aria-label="Photo of a garden wedding ceremony setting with white flowers and a grand piano"></div>
  <svg class="hero-curve" viewBox="0 0 849 112" preserveAspectRatio="none" aria-hidden="true">
    <path d="M0 70 C 220 125, 520 112, 849 30 L849 112 L0 112 Z" fill="#fdf6ee"/>
    <path d="M0 60 C 220 117, 520 104, 849 20" fill="none" stroke="#c48d58" stroke-width="3"/>
  </svg>
  <div class="couple-photo" role="img" aria-label="Soft photo of a bride and groom walking away holding hands, with pink bouquets in the foreground"></div>

  <header class="title">
    <span class="name bride">Anna</span>
    <span class="amp">&amp;</span>
    <span class="name groom">John's</span>
    <span class="event">Wedding</span>
  </header>

  <section class="details">
    <p class="date">Saturday, 05 July 2017</p>
    <p class="venue">HERON HALL</p>
    <p class="address">24 Maple Court, Ashbury NY 11500</p>
  </section>

  <section class="section prelude">
    <h2 class="pill">Prelude Ceremony</h2>
    <p class="song">Artist 1<span class="sep">|</span>1st Song title will be here....</p>
    <p class="song">Artist 2<span class="sep">|</span>2nd Song title will be here....</p>
    <p class="song">Artist 3<span class="sep">|</span>3rd Song title will be here....</p>
    <p class="song">Artist 4<span class="sep">|</span>4th Song title will be here....</p>
    <p class="song">Artist 5<span class="sep">|</span>5th Song title will be here....</p>
  </section>

  <section class="section canapes">
    <h2 class="pill">Canapes</h2>
    <p class="song">Artist 1<span class="sep">|</span>1st Song title will be here....</p>
    <p class="song">Artist 2<span class="sep">|</span>2nd Song title will be here....</p>
  </section>

  <section class="section ceremony">
    <h2 class="pill">Ceremony</h2>
    <h3 class="part">Processional</h3>
    <p class="song">Artist 1<span class="sep">|</span>1st Song title will be here....</p>
    <p class="song">Artist 2<span class="sep">|</span>2nd Song title will be here....</p>
    <h3 class="part">Signing of Papers</h3>
    <p class="song">Artist 1<span class="sep">|</span>1st Song title will be here....</p>
    <p class="song">Artist 2<span class="sep">|</span>2nd Song title will be here....</p>
    <h3 class="part">Recessional</h3>
    <p class="song">Artist 1<span class="sep">|</span>1st Song title will be here....</p>
  </section>

  <section class="section reception">
    <h2 class="pill">Reception</h2>
    <p class="song">Artist 1<span class="sep">|</span>1st Song title will be here....</p>
    <p class="song">Artist 2<span class="sep">|</span>2nd Song title will be here....</p>
  </section>

  <div class="brand">
    <span class="mark" aria-hidden="true"></span>
    <span class="name">TOLVERCADE</span>
  </div>
  <p class="web">www.tolvercade.com.au</p>

  <footer class="footer">
    <span class="link"><span class="dot"></span>instagram.com/tolvercademusic</span>
    <span class="link"><span class="dot"></span>facebook.com/tolvercadepianist</span>
    <span class="link"><span class="dot"></span>soundcloud.com/keyglow_nuptials</span>
  </footer>
</main>
</body>
</html>
```